Stationery Design for Family Law Firm
BROOK VESTAL, LLP
Stationery Design for Family Law Firm -
Creative Brief
Professional
Martin D. Vestal
Attorney & Counselor at Law
4187 Larkin Street San Diego, CA 92104
martin@brookvestal-law.example
www.brookvestal-law.example
Paper will be ivory. Please use large and small caps for name and "Attorney & Counselor" at Law. Sentence case for the rest.
Family Law I Guardianships I Conservatorships I Estate Planning

```html
<!DOCTYPE html>
<html lang="en">
<head>
<meta charset="utf-8">
<title>Brook Vestal, LLP — Business Card</title>
<link rel="stylesheet" href="https://fonts.googleapis.com/css2?family=Cinzel:wght@600&family=Open+Sans:wght@400;600;700&display=swap">
<style>
  :root {
    --backdrop: #3a3a3c;
    --card: #ffffff;
    --brand-blue: #1f5fa6;
    --brand-blue-light: #2f78c4;
    --edge-grey: #3b3d40;
    --ink: #2b2d30;
    --ink-soft: #55585c;
    --rule: #9a9da1;
  }
  html, body {
    margin: 0;
    width: 1200px;
    height: 780px;
    overflow: hidden;
    background: var(--backdrop);
  }
  .canvas {
    position: relative;
    width: 1200px;
    height: 780px;
  }
  .business-card {
    position: absolute;
    left: 100px;
    top: 100px;
    width: 1000px;
    height: 580px;
    border-radius: 34px;
    background: var(--card);
    overflow: hidden;
    box-shadow: 0 18px 40px rgba(0,0,0,.45);
  }
  .edge-bands {
    position: absolute;
    inset: 0;
  }
  .firm-name {
    position: absolute;
    left: 250px;
    top: 120px;
    display: flex;
    align-items: center;
    gap: 22px;
    font-family: "Cinzel", serif;
    font-weight: 600;
    font-size: 64px;
    letter-spacing: 1px;
    color: var(--brand-blue);
    line-height: 1;
  }
  .firm-name .mark-square {
    width: 34px;
    height: 34px;
    background: var(--brand-blue);
    flex: none;
  }
  .firm-tagline {
    position: absolute;
    left: 306px;
    top: 200px;
    font-family: "Cinzel", serif;
    font-weight: 600;
    font-size: 21px;
    letter-spacing: 1.5px;
    color: var(--ink);
  }
  .person {
    position: absolute;
    right: 460px;
    top: 340px;
    text-align: right;
    font-family: "Open Sans", sans-serif;
    color: var(--ink);
  }
  .person-name {
    font-weight: 700;
    font-size: 29px;
    color: var(--brand-blue);
    margin: 0 0 6px;
    font-variant: small-caps;
  }
  .person-title {
    font-weight: 600;
    font-size: 20px;
    margin: 0 0 22px;
    font-variant: small-caps;
  }
  .person-address {
    font-size: 19px;
    margin: 0;
    color: var(--ink-soft);
  }
  .divider {
    position: absolute;
    left: 560px;
    top: 340px;
    width: 1px;
    height: 130px;
    background: var(--rule);
  }
  .contact-list {
    position: absolute;
    left: 582px;
    top: 338px;
    margin: 0;
    padding: 0;
    list-style: none;
    font-family: "Open Sans", sans-serif;
    font-size: 19px;
    color: var(--ink-soft);
  }
  .contact-list li {
    display: flex;
    align-items: center;
    gap: 12px;
    height: 40px;
  }
  .contact-list svg {
    width: 20px;
    height: 20px;
    flex: none;
  }
</style>
</head>
<body>
<div class="canvas">
  <div class="business-card">
    <svg class="edge-bands" viewBox="0 0 1000 580" preserveAspectRatio="none" aria-hidden="true">
      <path d="M0 0 H60 Q20 290 60 580 H0 Z" fill="var(--edge-grey)"/>
      <path d="M0 0 H44 Q6 290 44 580 H0 Z" fill="var(--brand-blue)"/>
      <path d="M1000 0 H948 Q985 290 948 580 H1000 Z" fill="var(--edge-grey)"/>
      <path d="M1000 0 H962 Q998 290 962 580 H1000 Z" fill="var(--brand-blue-light)"/>
    </svg>

    <div class="firm-name"><span class="mark-square"></span>Brook Vestal, LLP</div>
    <div class="firm-tagline">Attorneys &amp; Counselors at Law</div>

    <div class="person">
      <p class="person-name">Martin D. Vestal</p>
      <p class="person-title">Attorney &amp; Counselor at Law</p>
      <p class="person-address">4187 Larkin Street San Diego, CA 92104</p>
    </div>

    <div class="divider"></div>

    <ul class="contact-list">
      <li>
        <svg viewBox="0 0 20 20" aria-hidden="true"><path d="M5 2 L8 2 L9 6 L7 8 Q9 12 12 13 L14 11 L18 12 L18 15 Q18 18 15 18 Q3 16 2 5 Q2 2 5 2 Z" fill="var(--brand-blue)"/></svg>
        (619) 555-0142
      </li>
      <li>
        <svg viewBox="0 0 20 20" aria-hidden="true"><circle cx="10" cy="10" r="8" fill="var(--brand-blue)"/><circle cx="10" cy="10" r="3.2" fill="none" stroke="#fff" stroke-width="1.8"/></svg>
        martin@brookvestal-law.example
      </li>
      <li>
        <svg viewBox="0 0 20 20" aria-hidden="true"><circle cx="10" cy="10" r="8" fill="none" stroke="var(--brand-blue)" stroke-width="1.8"/><ellipse cx="10" cy="10" rx="3.5" ry="8" fill="none" stroke="var(--brand-blue)" stroke-width="1.4"/><line x1="2" y1="10" x2="18" y2="10" stroke="var(--brand-blue)" stroke-width="1.4"/></svg>
        www.brookvestal-law.example
      </li>
    </ul>
  </div>
</div>
</body>
</html>
```